Company Postage Label

Design a postage label that measures: 16cm long x 9cm high with a sticky back to stick on boxes. Similar to the attached from Talvora Carriers.

Industry/Entity Type

Motorcycle Part

Colors

Designer to choose colors to be used in the design.

Requirements
Must have
• Company logo and address

```html
<!DOCTYPE html>
<html lang="en">
<head>
<meta charset="utf-8">
<title>Postage Label – Ridgeline Exhaust Works</title>
<link href="https://fonts.googleapis.com/css2?family=Roboto+Condensed:ital,wght@0,400;0,700;1,400&display=swap" rel="stylesheet">
<style>
  :root {
    --page-bg: #ececec;
    --label-frame: #6b6b6b;
    --panel-white: #ffffff;
    --rule: #7a7a7a;
    --text-grey: #5f5f5f;
    --brand-dark: #2b2b2b;
  }
  * { margin: 0; padding: 0; box-sizing: border-box; }
  html, body {
    width: 1200px; height: 900px; overflow: hidden;
    background: var(--page-bg);
    font-family: "Roboto Condensed", "Arial Narrow", sans-serif;
  }
  .postage-label {
    position: absolute; left: 144px; top: 194px;
    width: 913px; height: 513px;
    background: var(--label-frame);
    border-radius: 12px;
  }
  .sender-panel, .address-panel {
    position: absolute; top: 40px; height: 433px;
    background: var(--panel-white);
  }
  .sender-panel { left: 35px; width: 224px; }
  .address-panel { left: 275px; width: 610px; }

  .sender-rule {
    position: absolute; top: 16px; height: 401px;
    border-left: 1px solid var(--rule);
  }
  .sender-label {
    position: absolute; left: 24px; bottom: 14px;
    transform: rotate(-90deg); transform-origin: left bottom;
    font-size: 15px; color: var(--text-grey);
    translate: 18px 0;
  }

  .brand {
    position: absolute; left: 24px; top: 30px;
    display: flex; align-items: center; gap: 8px;
  }
  .brand-mark {
    width: 40px; height: 40px; border-radius: 50%;
    background: var(--brand-dark);
  }
  .brand-name {
    font-size: 17px; font-weight: 700; color: var(--brand-dark);
    line-height: 1.05; text-transform: uppercase;
  }
  .stamp-note {
    position: absolute; left: 432px; top: 20px;
    font-size: 17px; line-height: 1.1; color: var(--text-grey);
  }
  .address-rule {
    position: absolute; left: 22px; width: 567px;
    border-top: 1px solid var(--rule);
  }
  .to-label {
    position: absolute; left: 22px; top: 140px;
    font-size: 16px; font-style: italic; color: var(--text-grey);
  }
  .postcode-box {
    position: absolute; top: 332px; height: 48px;
    border-left: 1px solid var(--rule);
  }
  .print-code {
    position: absolute; right: 21px; top: 416px;
    font-size: 10px; color: var(--text-grey);
  }
</style>
</head>
<body>
  <div class="postage-label">
    <section class="sender-panel">
      <span class="sender-rule" style="left:27px"></span>
      <span class="sender-rule" style="left:69px"></span>
      <span class="sender-rule" style="left:111px"></span>
      <span class="sender-rule" style="left:154px"></span>
      <span class="sender-rule" style="left:196px"></span>
      <span class="sender-label">From</span>
    </section>

    <section class="address-panel">
      <div class="brand">
        <span class="brand-mark"></span>
        <span class="brand-name">Ridgeline<br>Exhaust Works</span>
      </div>
      <p class="stamp-note">Please affix stamps<br>before mailing</p>

      <span class="address-rule" style="top:136px"></span>
      <span class="to-label">To</span>
      <span class="address-rule" style="top:185px"></span>
      <span class="address-rule" style="top:234px"></span>
      <span class="address-rule" style="top:283px"></span>
      <span class="address-rule" style="top:332px"></span>
      <span class="address-rule" style="top:380px"></span>

      <span class="postcode-box" style="left:439px"></span>
      <span class="postcode-box" style="left:477px"></span>
      <span class="postcode-box" style="left:514px"></span>
      <span class="postcode-box" style="left:552px"></span>
      <span class="postcode-box" style="left:589px"></span>

      <span class="print-code">8835039 (PM90) May'04</span>
    </section>
  </div>
</body>
</html>
```